Startup in search for creative and funky label for a food product

We, Vindrossa Food Lab need a label for a new product: extra virgin oil from roasted sunflower seeds. The oil is produced at family gardens in sunny Kakheti region in Western Georgia.
Our goal is to introduce this new exclusive product, unknown in Western Europe. The test panels in Sweden liked the product and we hope to sell both for foodies and general public.
The feeling of the label shoud be both creative and exclusive. Maybe even funky, please see the file attached.

We would like to have the label in English and Swedish. Maybe we can do it in English first, since not all of you would understand Swedish, the Swedish design would be identical. The document below has both English and Swedish text.

We attachthe image of the bottle, please do not consider the label on the bottle, it is just an example.

Target Market(s)

General Market in Sweden and Europe. First priority: foddies, restaurants, specialized food stores.

Industry/Entity Type

Online Shopping

Requirements
Must have
• We would need the design in two languages, the same design for Swedish and English, but two separated labels. Once we agree on the English version, we can do the same for Swedish.
Nice to have
• Feeling of locally grown sunflowers, eye-catching.
Should not have
• Classic design for oil

```html
<!DOCTYPE html>
<html lang="en">
<head>
<meta charset="utf-8">
<title>Vindrossa Food Lab – Sunflower Oil Label</title>
<link rel="stylesheet" href="https://fonts.googleapis.com/css2?family=Amatic+SC:wght@700&family=Rye&display=swap">
<style>
  :root {
    --page: #ffffff;
    --sky: #0aa3e0;
    --sky-deep: #1f7fd0;
    --sunflower: #f6c935;
    --petal-light: #fbe27a;
    --petal-soft: rgba(251, 226, 122, 0.35);
    --leaf: #2fa040;
    --ink: #111111;
    --white: #ffffff;
  }
  * { margin: 0; padding: 0; box-sizing: border-box; }
  html, body {
    width: 1200px; height: 1200px; overflow: hidden;
    background: var(--page);
  }
  .label {
    position: absolute; left: 293px; top: 108px;
    width: 598px; height: 954px; overflow: hidden;
  }
  .label__sky {
    position: absolute; inset: 0;
    background: linear-gradient(160deg, var(--sky) 0%, #14aee6 45%, var(--sky-deep) 100%);
  }
  .label__premium {
    position: absolute; left: 0; top: 40px; width: 598px; height: 120px;
  }
  .label__premium text {
    font-family: "Rye", serif; font-size: 56px; fill: var(--white);
    letter-spacing: 2px;
  }
  .title {
    position: absolute; left: 0; width: 598px; text-align: center;
    font-family: "Amatic SC", cursive; font-weight: 700;
    color: var(--sunflower); line-height: 1; font-size: 122px;
    white-space: nowrap;
  }
  .title--extra { top: 122px; letter-spacing: 14px; padding-left: 14px; }
  .title--virgin { top: 222px; letter-spacing: 4px; padding-left: 4px; }
  .flower-mark {
    position: absolute; left: 135px; top: 328px; width: 205px; height: 190px;
    border-radius: 50%;
    background: radial-gradient(ellipse at 50% 55%, var(--petal-soft) 0%, rgba(251,226,122,0.18) 55%, transparent 72%);
  }
  .title--oil {
    top: 326px; left: 227px; width: auto; text-align: left;
    letter-spacing: 12px;
  }
  .origin {
    position: absolute; left: 0; width: 598px; text-align: center;
    font-family: "Amatic SC", cursive; font-weight: 700; color: var(--ink);
    white-space: nowrap;
  }
  .origin--main { top: 530px; font-size: 50px; line-height: 40px; letter-spacing: 2px; }
  .origin--sub { top: 621px; font-size: 28px; line-height: 26px; letter-spacing: 1.5px; }
  .meadow {
    position: absolute; left: 0; top: 672px; width: 598px; height: 282px;
    background: linear-gradient(180deg, rgba(246,201,53,0) 0%, var(--sunflower) 20%, var(--petal-light) 55%, var(--leaf) 100%);
  }
  .claim {
    position: absolute; width: 170px; text-align: center;
    font-family: "Amatic SC", cursive; font-weight: 700;
    font-size: 36px; line-height: 36px; letter-spacing: 1px; color: var(--ink);
    white-space: nowrap; transform-origin: 50% 50%;
  }
  .claim--unrefined { left: 87px; top: 706px; transform: rotate(34deg); }
  .claim--natural { left: 351px; top: 710px; transform: rotate(-32deg); }
  .brand {
    position: absolute; left: 250px; top: 716px; width: 104px; height: 104px;
    border-radius: 50%; background: var(--ink);
    display: flex; align-items: center; justify-content: center; text-align: center;
  }
  .brand__name {
    font-family: "Amatic SC", cursive; font-weight: 700; font-size: 24px;
    color: var(--sunflower); line-height: 1;
  }
  .volume {
    position: absolute; left: 0; top: 877px; width: 592px; text-align: center;
    font-family: "Amatic SC", cursive; font-weight: 700; font-size: 44px;
    line-height: 1; color: var(--ink);
  }
</style>
</head>
<body>
  <main class="label">
    <div class="label__sky" role="img" aria-label="Hand-painted blue brushstroke sky background"></div>

    <svg class="label__premium" viewBox="0 0 598 120" aria-label="Premium">
      <defs><path id="premium-arc" d="M110 110 Q299 10 488 110"/></defs>
      <text><textPath href="#premium-arc" startOffset="50%" text-anchor="middle">PREMIUM</textPath></text>
    </svg>

    <div class="flower-mark" role="img" aria-label="Drawn sunflower petals around the O of Oil"></div>
    <h1>
      <span class="title title--extra">EXTRA</span>
      <span class="title title--virgin">VIRGIN</span>
      <span class="title title--oil">OIL</span>
    </h1>

    <div class="meadow" role="img" aria-label="Illustrated sunflowers with green leaves"></div>

    <p class="origin origin--main">FROM ROASTED<br>SUNFLOWER SEEDS</p>
    <p class="origin origin--sub">FROM FAMILY GARDENS<br>IN KAKHETI</p>

    <span class="claim claim--unrefined">UNREFINED</span>
    <span class="claim claim--natural">ALL NATURAL</span>
    <div class="brand"><span class="brand__name">Vindrossa<br>Food Lab</span></div>
    <p class="volume">260 ML</p>
  </main>
</body>
</html>
```